Design some Business Cards for Web Company (Vector / AI)

Need a business card design, front and back, standard size :

(US)
Bleed size: 95.25 × 57.15 mm (3.75 × 2.25 in) (1⁄8 in bleeds)
Standard cut size: 89 × 51 mm (3.5 × 2 in)

Horizontal or vertical (portrait or landscape) layouts are both fine and will be considered.

This contest is *guaranteed* a winner. View our past contests to verify we *always* award a winner, so design to win this!

If your work is compelling and well done, we will give you more work to follow - this is also something of a test to find a good designer for future projects.

This is for a web development company, offering web, mobile and app development. You can view the site here to get an idea of the culture and presentation of the company in general : [url removed, login to view]

You will see in the body text of the site that it is a fun / irreverent, but still professional company. The design should be smart and sleek. The cards are full color on both sides, use that in a clever way.

Attached is the current logo for you use. You will have to convert it into vector (very simple, few circles and a gradient).

The winner of this contest will be the one that presents the best design that follows these creative ideas.

```html
<!DOCTYPE html>
<html lang="en">
<head>
<meta charset="utf-8">
<title>Brightpane Business Cards</title>
<link rel="stylesheet" href="https://fonts.googleapis.com/css2?family=Russo+One&family=Arimo:wght@700&family=Tinos&family=Permanent+Marker&display=swap">
<style>
  :root {
    --stage: #3d3d3d;
    --stage-edge: #1f1f1f;
    --card-black: #050505;
    --panel-black: #0a0a0a;
    --paper-light: #e6e6e6;
    --paper-mid: #bdbdbd;
    --paper-dark: #9a9a9a;
    --ink: #111111;
    --ink-soft: #2a2a2a;
    --white: #ffffff;
    --accent: #67c8de;
  }
  * { margin: 0; padding: 0; box-sizing: border-box; }
  html, body { width: 1200px; height: 684px; overflow: hidden; }
  body {
    background: var(--stage);
    position: relative;
    font-family: "Arimo", Arial, sans-serif;
  }
  .stage {
    position: absolute; inset: 0;
    border: 2px solid var(--stage-edge);
  }

  /* Front card */
  .card-front {
    position: absolute;
    left: 73px; top: 203px;
    width: 523px; height: 333px;
    background: var(--card-black);
    box-shadow: 0 4px 14px rgba(0,0,0,.45);
  }
  .card-front .brand {
    position: absolute;
    left: 160px; top: 318px;
    display: flex; align-items: center; gap: 14px;
  }
  .card-front .brand {
    left: 87px; top: 115px;
  }
  .brand-square {
    width: 58px; height: 58px;
    background: var(--white);
  }
  .card-front .brand-name {
    font-family: "Russo One", sans-serif;
    font-size: 36px;
    color: var(--white);
    letter-spacing: 0.5px;
  }
  .card-front .website {
    position: absolute;
    left: 0; right: 0; top: 254px;
    text-align: center;
    font-family: "Tinos", "Times New Roman", serif;
    font-size: 23px;
    color: var(--white);
  }

  /* Back card */
  .card-back {
    position: absolute;
    left: 637px; top: 197px;
    width: 512px; height: 306px;
    background: linear-gradient(100deg, var(--paper-light) 0%, #d6d6d6 35%, var(--paper-mid) 75%, var(--paper-dark) 100%);
    box-shadow: 0 4px 14px rgba(0,0,0,.45);
    overflow: hidden;
  }
  .side-strip {
    position: absolute; left: 0; top: 0; bottom: 0; width: 50px;
    background: linear-gradient(90deg, #f2f2f2, #cfcfcf);
  }
  .side-band {
    position: absolute; left: 50px; top: 0; bottom: 0; width: 73px;
    background: var(--panel-black);
  }
  .side-band .band-mark {
    position: absolute; left: 14px; top: 30px;
    width: 42px; height: 42px; border-radius: 50%;
    background: var(--accent);
  }
  .side-band svg.band-curve {
    position: absolute; left: 0; top: 70px;
  }
  .card-back .brand-name {
    position: absolute; left: 140px; top: 34px;
    font-family: "Russo One", sans-serif;
    font-size: 30px;
    color: var(--ink-soft);
  }
  .card-back .person-name {
    position: absolute; left: 130px; top: 101px;
    font-family: "Permanent Marker", cursive;
    font-size: 24px;
    color: var(--ink);
    letter-spacing: 1px;
  }
  .contact-row {
    position: absolute; left: 110px;
    display: flex; align-items: flex-start; gap: 12px;
  }
  .contact-row.address { top: 155px; }
  .contact-row.phones { top: 201px; }
  .contact-row svg { flex: none; margin-top: 6px; }
  .contact-lines {
    font-size: 16px; line-height: 21px;
    color: var(--ink);
  }
  .card-back .email {
    position: absolute; right: 50px; top: 263px;
    font-family: "Permanent Marker", cursive;
    font-size: 18px;
    color: var(--white);
    text-shadow: 1px 1px 0 #222, 2px 2px 2px rgba(0,0,0,.6);
  }
</style>
</head>
<body>
  <main class="stage">
    <section class="card-front" aria-label="Card front">
      <div class="brand">
        <span class="brand-square" aria-hidden="true"></span>
        <span class="brand-name">BRIGHTPANE</span>
      </div>
      <p class="website">www.brightpane.com</p>
    </section>

    <section class="card-back" aria-label="Card back">
      <div class="side-strip"></div>
      <div class="side-band">
        <span class="band-mark" aria-hidden="true"></span>
        <svg class="band-curve" width="73" height="20" viewBox="0 0 73 20" aria-hidden="true">
          <path d="M0 4 Q36 22 73 4" fill="none" stroke="#ffffff" stroke-width="2"/>
        </svg>
      </div>
      <div class="brand-name">BRIGHTPANE</div>
      <div class="person-name">MARLA QUINN</div>

      <div class="contact-row address">
        <svg width="14" height="18" viewBox="0 0 14 18" aria-hidden="true">
          <path d="M7 0C3.1 0 0 3.1 0 7c0 5 7 11 7 11s7-6 7-11c0-3.9-3.1-7-7-7zm0 9.5A2.5 2.5 0 1 1 7 4.5a2.5 2.5 0 0 1 0 5z" fill="#ffffff"/>
        </svg>
        <div class="contact-lines">4417 N Alder Blvd,<br>Denton TX 76201</div>
      </div>

      <div class="contact-row phones">
        <svg width="14" height="18" viewBox="0 0 14 18" aria-hidden="true">
          <path d="M3 0.5l2.6 3.6-1.6 2c.9 2.4 2.4 4.3 4.4 5.6l1.8-1.4 3.3 2.8-1.6 3.2C6.5 16 1 10 .6 3.4L3 .5z" fill="#ffffff"/>
        </svg>
        <div class="contact-lines">+(940) 555 0172<br>+(800) 555 0349</div>
      </div>

      <div class="email">marla.quinn@brightpane.com</div>
    </section>
  </main>
</body>
</html>
```